Honey Packaging Label Design

The honey packaging label should be designed in a transparent look. The design concept for this product should be natural and healthy. Please include the logo and nutrition fact in the attachment. The size for the label is 9cm width by 5cm height. Please also include the information of our company. Since the bar code is not ready yet, please leave space for the bar code.
Torvel International Trading Group Inc.
#2734 - 816 Pemberly St., Vancouver, V5K 2R8
Tel: 1-604-512-8273/8274
Since our company's logo for the packaging is still not finished yet, so please leave space for our logo, and we will be able to add it on later.

Please be creative.

If you have any question you can call at 1-604-512-8273/8274 or e-mail to marthak@torvelmail.ca

Thank you!

Target Market(s)

Supermarket, wholesale

Industry/Entity Type

Product

Requirements
Must have
• Nutrition facts, bar code, logo, address, transparent, modern look design, geometry design.
Nice to have
• Bees, flowers
Should not have
• Traditional design.

```html
<!DOCTYPE html>
<html lang="en">
<head>
<meta charset="utf-8">
<title>Canadian White Honey – Label</title>
<link rel="stylesheet" href="https://fonts.googleapis.com/css2?family=Montserrat:wght@500;700&family=Arimo:wght@400;700&family=Libre+Baskerville:ital@1&display=swap">
<style>
  :root {
    --canvas: #f4f2ee;
    --label-black: #0d0c0b;
    --gold: #f5c518;
    --gold-deep: #e39a0c;
    --gold-light: #ffd84a;
    --silver-hi: #ffffff;
    --silver-lo: #a9a9ab;
    --grey-text: #d9d9d9;
    --panel-ink: #1a1405;
  }
  * { box-sizing: border-box; margin: 0; padding: 0; }
  html, body { width: 1200px; height: 889px; overflow: hidden; }
  body { background: var(--canvas); position: relative; font-family: "Arimo", Arial, sans-serif; }

  .label {
    position: absolute;
    background: var(--label-black);
    box-shadow: 0 6px 22px rgba(0,0,0,.18);
    overflow: hidden;
  }
  .label--front { left: 80px; top: 328px; width: 466px; height: 260px; }
  .label--back { left: 658px; top: 333px; width: 467px; height: 257px; }

  /* front */
  .brand-mark {
    position: absolute; left: 173px; top: 18px; width: 120px; height: 72px;
    border-radius: 50%;
    background: linear-gradient(135deg, var(--gold-light) 0%, var(--gold) 45%, var(--gold-deep) 100%);
  }
  .product-name {
    position: absolute; left: 0; right: 0; top: 100px; text-align: center;
    font-family: "Montserrat", sans-serif; font-weight: 700; font-size: 76px; letter-spacing: 1px;
    line-height: 1;
    background: linear-gradient(180deg, var(--silver-hi) 30%, var(--silver-lo) 100%);
    -webkit-background-clip: text; background-clip: text; color: transparent;
  }
  .variety {
    position: absolute; left: 0; right: 0; top: 179px;
    display: flex; justify-content: center; align-items: center; gap: 10px;
    font-family: "Montserrat", sans-serif; font-weight: 500; font-size: 13px; letter-spacing: 1px; color: var(--grey-text);
    line-height: 16px;
  }
  .hex-row { display: flex; }
  .gold-bands { position: absolute; left: 0; top: 216px; width: 100%; height: 26px; }
  .net-weight {
    position: absolute; left: 210px; top: 210px; width: 48px; height: 40px;
    display: flex; align-items: center; justify-content: center;
    font-family: "Montserrat", sans-serif; font-size: 10px; font-weight: 500; color: var(--panel-ink);
  }
  .net-weight svg { position: absolute; inset: 0; }
  .net-weight span { position: relative; }

  /* back */
  .nutrition {
    position: absolute; left: 22px; top: 17px; width: 191px; height: 221px;
    background: var(--gold); border: 2px solid var(--gold-light); border-radius: 8px;
    box-shadow: inset 0 0 0 2px var(--label-black);
    color: var(--panel-ink); font-size: 7.5px; line-height: 1.27; padding: 6px 8px;
  }
  .nutrition h2 { font-size: 10px; font-weight: 700; line-height: 1.15; }
  .nutrition .rule { border-top: 1px solid var(--panel-ink); margin: 3px 0; }
  .nutrition .rule--thick { border-top-width: 3px; }
  .nutrition .row { display: flex; justify-content: space-between; }
  .nutrition .indent { padding-left: 10px; }
  .nutrition p { margin-top: 6px; }

  .story {
    position: absolute; left: 232px; top: 20px; width: 230px; text-align: center;
    font-family: "Libre Baskerville", serif; font-style: italic; color: #fff; font-size: 8.4px; line-height: 1.85;
  }
  .story h3 { color: var(--gold); font-weight: 400; font-size: 9.2px; margin-bottom: 2px; }
  .company {
    position: absolute; left: 232px; top: 196px; width: 230px; text-align: center;
    font-style: normal; font-size: 9px; line-height: 1.4; color: var(--grey-text);
  }
</style>
</head>
<body>

  <section class="label label--front" aria-label="Front label">
    <div class="brand-mark" role="img" aria-label="Space for the golden brand emblem"></div>
    <h1 class="product-name">HONEY</h1>
    <div class="variety">
      <span class="hex-row" aria-hidden="true">
        <svg width="20" height="8" viewBox="0 0 20 8"><polygon fill="#f5c518" points="2,0 6,0 8,4 6,8 2,8 0,4"/><polygon fill="#f5c518" points="12,0 16,0 18,4 16,8 12,8 10,4"/></svg>
      </span>
      <span>Canadian White Honey</span>
      <span class="hex-row" aria-hidden="true">
        <svg width="20" height="8" viewBox="0 0 20 8"><polygon fill="#f5c518" points="2,0 6,0 8,4 6,8 2,8 0,4"/><polygon fill="#f5c518" points="12,0 16,0 18,4 16,8 12,8 10,4"/></svg>
      </span>
    </div>
    <svg class="gold-bands" viewBox="0 0 466 26" preserveAspectRatio="none" aria-hidden="true">
      <g stroke="#f5c518" stroke-width="1.5">
        <line x1="0" y1="3" x2="466" y2="3"/>
        <line x1="0" y1="9" x2="466" y2="9"/>
        <line x1="0" y1="16" x2="466" y2="16"/>
        <line x1="0" y1="22" x2="466" y2="22"/>
      </g>
    </svg>
    <div class="net-weight">
      <svg viewBox="0 0 48 40" aria-hidden="true"><polygon points="12,1 36,1 47,20 36,39 12,39 1,20" fill="#f5c518" stroke="#0d0c0b" stroke-width="2"/></svg>
      <span>12OZ.</span>
    </div>
  </section>

  <section class="label label--back" aria-label="Back label">
    <div class="nutrition">
      <h2>NUTRITION FACT<br>VALEUR NUTRITIVE</h2>
      <div class="rule"></div>
      <div>Per 1 tablespoon (20 g)<br>Pour 1 cuillère à table (20 g)</div>
      <div class="rule rule--thick"></div>
      <div class="row"><span>Amount</span><span>% Daily Values</span></div>
      <div class="row"><span>Teneur</span><span>% valeur quotidienne</span></div>
      <div>Calories / Calories 60</div>
      <div class="row"><span>Fat / Lipides 0 g</span><span>0 %</span></div>
      <div class="row"><span>Carbohydrate / Glucides</span><span>17 g 6 %</span></div>
      <div class="indent">Sugars / Sucres 16 g</div>
      <div>Protein / Protéines 0 g</div>
      <p>Not a significant source of saturated fat, trans fat, Cholesterol, sodium, fibers, vitamin A, vitamin C, Calcium or iron.</p>
      <div class="rule"></div>
      <div>Source négligeable de lipids saturés, lipids trans, cholesterol, sodium, fibres, vitamine A, vitamine C, calcium et fer.</div>
    </div>

    <div class="story">
      <h3>Lorem ipsum dolor sit amet</h3>
      Consectetuer adipiscing elit, sed diam nonummy nibh euismod tincidunt ut laoreet dolore magna aliquam erat volutpat. Ut wisi enim ad minim veniam, quis nostrud exerci tation ullamcorper suscipit lobortis nisl ut aliquip ex ea commodo consequat. Duis autem vel eum iriure dolor in hendrerit.
    </div>

    <address class="company">
      Torvel International Trading Group Inc.<br>
      #2734 - 816 Pemberly St.,<br>
      Vancouver, V5K 2R8<br>
      Tel: 1-604-512-8273/8274
    </address>
  </section>

</body>
</html>
```